Builder Business Card Design

I need a design a business card that is different from others and use as a logo for other prints. I'm a builder that build domestic/residential home new, renovate & malty unit development . I would like a Slogan that in unique . I look forward to talk to someone about it.

Industry/Entity Type

Business

Contact Information for Business Card

Tallowbrook homes, Colin Marchetti 0487 512 904 , DB-U 74129

```html
<!DOCTYPE html>
<html lang="en">
<head>
<meta charset="utf-8">
<title>Tallowbrook Homes – Business Card</title>
<link rel="stylesheet" href="https://fonts.googleapis.com/css2?family=Barlow+Semi+Condensed:wght@500;600;700&display=swap">
<style>
  :root {
    --backdrop: #e4e4e4;
    --card: #5a1115;
    --gold: #f3b61f;
    --white: #ffffff;
  }
  * { margin: 0; padding: 0; box-sizing: border-box; }
  html, body {
    width: 1200px;
    height: 900px;
    overflow: hidden;
    background: var(--backdrop);
  }
  .stage {
    width: 1200px;
    height: 900px;
    display: flex;
    align-items: center;
    justify-content: center;
  }
  .business-card {
    position: relative;
    width: 780px;
    height: 450px;
    background: var(--card);
    font-family: "Barlow Semi Condensed", "Arial Narrow", sans-serif;
    box-shadow: 0 6px 18px rgba(0, 0, 0, 0.25);
  }
  .brand {
    position: absolute;
    left: 96px;
    top: 140px;
    display: flex;
    align-items: center;
    gap: 16px;
  }
  .brand-mark {
    width: 26px;
    height: 26px;
    background: var(--gold);
  }
  .brand-name {
    color: var(--gold);
    font-weight: 700;
    font-size: 50px;
    letter-spacing: 1px;
    text-transform: uppercase;
    line-height: 1;
  }
  .contact {
    position: absolute;
    left: 330px;
    top: 290px;
    line-height: 1.15;
  }
  .contact-name {
    color: var(--gold);
    font-weight: 700;
    font-size: 32px;
    letter-spacing: 1px;
    text-transform: uppercase;
  }
  .contact-details {
    color: var(--white);
    font-weight: 500;
    font-size: 30px;
    letter-spacing: 2px;
  }
  .divider {
    color: var(--gold);
    margin: 0 10px;
  }
</style>
</head>
<body>
  <main class="stage">
    <section class="business-card" aria-label="Tallowbrook Homes business card">
      <div class="brand">
        <span class="brand-mark" aria-hidden="true"></span>
        <span class="brand-name">Tallowbrook Homes</span>
      </div>
      <div class="contact">
        <p class="contact-name">Colin Marchetti</p>
        <p class="contact-details">0487 512 904<span class="divider">//</span>DB-U 74129</p>
      </div>
    </section>
  </main>
</body>
</html>
```